Letterhead to coordinate with business card

I am needing a docx template and print file for a letterhead to co-ordinate with my newly designed logo and business card.

```html
<!DOCTYPE html>
<html lang="en">
<head>
<meta charset="utf-8">
<title>Harbour Plan Services – Letterhead</title>
<link rel="stylesheet" href="https://fonts.googleapis.com/css2?family=Quicksand:wght@500;600&display=swap">
<style>
  :root {
    --backdrop: #e4e4e4;
    --paper: #ffffff;
    --ink: #333a45;
    --navy: #2f3542;
    --teal: #138a80;
    --magenta: #a8306a;
    --plum: #7a2b6c;
    --signature: #dcdee3;
  }
  * { box-sizing: border-box; margin: 0; padding: 0; }
  html, body {
    width: 1200px; height: 1200px; overflow: hidden;
    background: var(--backdrop);
    font-family: "Quicksand", sans-serif;
    font-weight: 500;
    color: var(--ink);
  }
  .letterhead {
    position: absolute; left: 307px; top: 76px;
    width: 738px; height: 1044px;
    background: var(--paper);
    overflow: hidden;
  }
  .header-band {
    position: absolute; left: 0; top: 0; width: 100%; height: 48px;
    background: linear-gradient(90deg, var(--navy) 0%, var(--navy) 55%, var(--plum) 100%);
  }
  .footer-band {
    position: absolute; left: 0; bottom: 0; width: 100%; height: 72px;
    background: linear-gradient(90deg, var(--plum) 0%, var(--navy) 45%, var(--navy) 70%, var(--teal) 100%);
  }

  .brand {
    position: absolute; left: 59px; top: 59px; width: 212px;
    display: flex; flex-direction: column; align-items: center;
  }
  .brand-square { width: 96px; height: 90px; background: var(--magenta); }
  .brand-name {
    margin-top: 10px;
    font-size: 21px; font-weight: 600; line-height: 1.1;
    color: var(--magenta); text-align: center;
  }

  .contact {
    position: absolute; left: 491px; top: 80px;
    list-style: none; font-size: 9.5px; line-height: 15px; color: var(--ink);
  }
  .contact li { display: flex; align-items: center; gap: 6px; }
  .contact svg { width: 8px; height: 8px; fill: var(--teal); flex: none; }

  .recipient {
    position: absolute; left: 66px; top: 231px;
    font-size: 13px; line-height: 19.9px; font-style: normal;
  }
  .salutation { position: absolute; left: 66px; top: 371px; font-size: 13px; line-height: 19.9px; }
  .letter-body {
    position: absolute; left: 66px; top: 411px; width: 599px;
    font-size: 13px; line-height: 19.9px; text-align: justify;
  }
  .signature {
    position: absolute; left: 66px; top: 743px; width: 185px; height: 45px;
    background: var(--signature); border-radius: 4px;
  }

  .footer-pin { position: absolute; left: 88px; top: 984px; width: 7px; height: 10px; fill: var(--teal); }
  .website {
    position: absolute; right: 62px; top: 1000px;
    font-size: 11px; line-height: 14px; color: #ffffff;
  }
  .website span { color: #2bb3a6; }
</style>
</head>
<body>
  <article class="letterhead">
    <div class="header-band" role="img" aria-label="Decorative header band in navy and plum"></div>

    <div class="brand">
      <div class="brand-square"></div>
      <p class="brand-name">Harbour Plan<br>Services</p>
    </div>

    <ul class="contact">
      <li><svg viewBox="0 0 24 24"><path d="M6.6 10.8a15.1 15.1 0 0 0 6.6 6.6l2.2-2.2a1 1 0 0 1 1-.25 11.4 11.4 0 0 0 3.6.57 1 1 0 0 1 1 1V20a1 1 0 0 1-1 1A17 17 0 0 1 3 4a1 1 0 0 1 1-1h3.5a1 1 0 0 1 1 1c0 1.25.2 2.45.57 3.57a1 1 0 0 1-.25 1z"/></svg>0400 218 604</li>
      <li><svg viewBox="0 0 24 24"><path d="M2 5h20v14H2z M4 7v.5l8 5 8-5V7l-8 5z" fill-rule="evenodd"/></svg>info@harbourplanservices.com.au</li>
      <li><svg viewBox="0 0 24 24"><path d="M12 2a7 7 0 0 0-7 7c0 5 7 13 7 13s7-8 7-13a7 7 0 0 0-7-7zm0 9.5A2.5 2.5 0 1 1 12 6.5a2.5 2.5 0 0 1 0 5z"/></svg>PO Box 42, Lakeside NSW 2000</li>
    </ul>

    <address class="recipient">
      Mr. John Doe<br>
      President<br>
      Summit Ledger Partners<br>
      111 Street Name,<br>
      City State, 12345
    </address>

    <p class="salutation">Dear</p>

    <div class="letter-body">
      <p>Lorem ipsum dolor sit amet, consectetur adipiscing elit. Aenean ut ipsum eget massa hendrerit vestibulum vel in velit. Donec pretium neque velit.</p>
      <p>Aliquam porta lectus nec mauris ornare venenatis. Vivamus non est turpis, et cursus sem. Mauris vehicula erat in diam auctor at bibendum nisl lacinia.</p>
      <p>Morbi imperdiet neque vehicula nunc convallis gravida. Vestibulum iaculis pretium placerat. Integer consequat, est sit amet facilisis eleifend, nibh nibh varius orci, eget dapibus arcu dui non purus. Pellentesque in magna mauris. Duis enim sapien, dictum vitae condimentum a, pulvinar vel lacus. Mauris et molestie nibh. Vestibulum vitae nulla at metus elementum porta sit amet interdum elit. Nulla sollicitudin neque eu nulla volutpat congue.</p>
      <p>Etiam pellentesque, velit id dapibus fermentum, turpis sapien ornare dui, ac tincidunt ligula odio congue purus. Nunc sed ante dui, in porta lectus. Cras nec sem lorem. In hac habitasse platea dictumst. Maecenas id diam quis dui porta tristique. Sed id egestas felis. Donec ullamcorper mattis posuere. Phasellus fermentum eleifend tortor vel dapibus. Vestibulum ante ipsum.</p>
    </div>

    <div class="signature" role="img" aria-label="Handwritten signature of the sender"></div>

    <div class="footer-band" role="img" aria-label="Decorative footer band in plum, navy and teal"></div>
    <svg class="footer-pin" viewBox="0 0 24 32" aria-hidden="true"><path d="M12 0a11 11 0 0 0-11 11c0 8 11 21 11 21s11-13 11-21A11 11 0 0 0 12 0zm0 15a4 4 0 1 1 0-8 4 4 0 0 1 0 8z"/></svg>
    <p class="website">www.<span>harbourplanservices</span>.com</p>
  </article>
</body>
</html>
```